Criação de Folder para Alimentos & Bebidas
A empresa queria:
" importamos produtos com nossas marcas e distribuimos para supermercdos e distribuidores "

```html
<!DOCTYPE html>
<html lang="pt-BR">
<head>
<meta charset="UTF-8">
<title>Harbor Foods – Folder</title>
<link rel="stylesheet" href="https://fonts.googleapis.com/css2?family=Open+Sans:wght@400;600;700;800&display=swap">
<style>
  :root {
    --red: #d6141c;
    --red-dark: #b00d14;
    --yellow: #ffd21a;
    --yellow-deep: #f5b400;
    --text: #7a7a7a;
    --ink: #333333;
    --paper: #ffffff;
    --backdrop: #ececec;
    --rule: #e3e3e3;
  }
  * { box-sizing: border-box; margin: 0; padding: 0; }
  html, body { width: 1200px; height: 1200px; overflow: hidden; }
  body {
    background: var(--backdrop);
    font-family: "Open Sans", Arial, sans-serif;
    position: relative;
  }
  .spread {
    position: absolute;
    left: 80px; top: 180px;
    width: 1040px; height: 840px;
    display: flex;
  }
  .page {
    position: relative;
    width: 520px; height: 840px;
    background: var(--paper);
    overflow: hidden;
  }
  .page-art { position: absolute; inset: 0; width: 100%; height: 100%; }

  /* left page */
  .hero-photo {
    position: absolute;
    left: 70px; top: 22px;
    width: 340px; height: 230px;
    background: radial-gradient(ellipse at 45% 40%, #ffffff 0%, #f1eee8 45%, #c9a27a 100%);
    border-radius: 4px;
  }
  .about-title {
    position: absolute;
    top: 300px; left: 0; width: 100%;
    text-align: center;
    color: var(--red);
    font-size: 22px; font-weight: 700;
  }
  .about-text {
    position: absolute;
    top: 345px; left: 45px; width: 430px;
    color: var(--text);
    font-size: 12.5px; line-height: 1.55;
  }
  .about-text p { margin-bottom: 18px; }
  .about-text .lead { color: var(--red); font-weight: 600; }
  .brand {
    position: absolute;
    top: 725px; left: 0; width: 100%;
    display: flex; align-items: center; justify-content: center; gap: 10px;
    font-size: 30px; font-weight: 600; color: var(--ink);
    letter-spacing: -0.5px;
  }
  .brand-dot { width: 14px; height: 14px; border-radius: 50%; background: var(--red); }

  /* right page */
  .tagline {
    position: absolute;
    top: 22px; right: 22px;
    width: 320px; padding: 10px 14px;
    background: var(--red);
    color: #fff;
    font-size: 20px; font-weight: 600; line-height: 1.2;
    text-align: center;
  }
  .products { position: absolute; top: 150px; left: 28px; width: 470px; }
  .product {
    height: 160px;
    border-bottom: 1px solid var(--rule);
    padding-top: 6px;
  }
  .product:last-child { border-bottom: none; }
  .product-label {
    color: var(--red);
    font-size: 11.5px; font-weight: 700; line-height: 1.25;
    margin-bottom: 6px;
  }
  .product-body { display: flex; gap: 22px; align-items: flex-start; }
  .product-photo {
    flex: none;
    width: 96px; height: 96px;
    border: 5px solid var(--yellow);
    box-shadow: 0 0 0 1px var(--yellow-deep);
  }
  .photo-lamb { background: linear-gradient(135deg, #7a2a20, #c44a3a 55%, #e8d9c8); }
  .photo-beef { background: linear-gradient(135deg, #8b1a1f, #c8323a 55%, #e28a8a); }
  .photo-fish { background: linear-gradient(135deg, #5b6770, #b9c3c8 55%, #e7c24a); }
  .photo-fries { background: linear-gradient(135deg, #f2b01e, #f7d35b 55%, #c22a1c); }
  .product-text {
    color: var(--text);
    font-size: 12.5px; line-height: 1.55;
    padding-top: 8px;
  }
</style>
</head>
<body>
  <main class="spread">
    <section class="page page-left">
      <svg class="page-art" viewBox="0 0 520 840" preserveAspectRatio="none" aria-hidden="true">
        <path d="M0 0 H520 V40 C420 120 320 230 0 250 Z" fill="var(--yellow)"/>
        <path d="M0 250 C320 230 420 120 520 40 V75 C430 150 330 262 0 272 Z" fill="var(--red)"/>
        <path d="M0 800 C180 780 340 790 520 770 V790 C340 805 180 800 0 815 Z" fill="var(--yellow)"/>
        <path d="M0 815 C180 800 340 805 520 790 V840 H0 Z" fill="var(--red)"/>
      </svg>
      <div class="hero-photo" role="img" aria-label="Foto de um chef sorridente segurando um prato de carne assada"></div>
      <h2 class="about-title">Sobre nossa empresa</h2>
      <div class="about-text">
        <p class="lead">Lorem ipsum dolor sit amet, consectetur adipiscing elit.<br>Phasellus iaculis bibendum auctor. Mauris tempus at nisl vitae lobortis.</p>
        <p>Sed commodo nec enim vitae vestibulum. Cras porta leo eget orci elementum tincidunt. Vivamus aliquam ligula non sapien auctor, nec cursus neque sagittis. Vestibulum id varius nulla. Duis molestie libero quis nibh feugiat gravida. Aenean et neque a ligula luctus facilisis nec sit amet dui.</p>
        <p>Duis auctor arcu a dictum suscipit. Cras nisl odio, tempor eu neque id, sodales laoreet neque. Pellentesque pulvinar ligula eget enim porta, non porttitor tellus convallis. Sed eget elit ac quam elementum ornare ut nec risus. Pellentesque aliquet ultricies dolor, vitae viverra arcu ullamcorper eu. Pellentesque eu mi et sapien faucibus maximus et a mi.</p>
      </div>
      <div class="brand"><span class="brand-dot"></span><span>Harbor Foods</span></div>
    </section>

    <section class="page page-right">
      <svg class="page-art" viewBox="0 0 520 840" preserveAspectRatio="none" aria-hidden="true">
        <path d="M0 0 H190 C130 40 70 60 0 75 Z" fill="var(--yellow)"/>
        <path d="M0 40 C70 30 130 15 170 0 H205 C150 45 80 75 0 95 Z" fill="var(--red)"/>
        <path d="M0 770 C180 790 340 780 520 800 V815 C340 800 180 808 0 790 Z" fill="var(--yellow)"/>
        <path d="M0 790 C180 808 340 800 520 815 V840 H0 Z" fill="var(--red)"/>
      </svg>
      <div class="tagline">Produtos especiais para melhorar o seu dia!</div>
      <div class="products">
        <article class="product">
          <div class="product-label">Cordeiros<br>linha Prime Lamb</div>
          <div class="product-body">
            <div class="product-photo photo-lamb" role="img" aria-label="Foto de cortes de carne de cordeiro"></div>
            <p class="product-text">Lorem ipsum dolor sit amet,<br>consectetur adipiscing elit.<br>Phasellus iaculis bibendum auctor.<br>Mauris tempus at nisl vitae lobortis.</p>
          </div>
        </article>
        <article class="product">
          <div class="product-label">Bovinos<br>linha Harbor Beef</div>
          <div class="product-body">
            <div class="product-photo photo-beef" role="img" aria-label="Foto de carne bovina fresca"></div>
            <p class="product-text">Lorem ipsum dolor sit amet,<br>consectetur adipiscing elit.<br>Phasellus iaculis bibendum auctor.<br>Mauris tempus at nisl vitae lobortis.</p>
          </div>
        </article>
        <article class="product">
          <div class="product-label">Pescado<br>linha Harbor Fish</div>
          <div class="product-body">
            <div class="product-photo photo-fish" role="img" aria-label="Foto de peixe inteiro com limão"></div>
            <p class="product-text">Lorem ipsum dolor sit amet,<br>consectetur adipiscing elit.<br>Phasellus iaculis bibendum auctor.<br>Mauris tempus at nisl vitae lobortis.</p>
          </div>
        </article>
        <article class="product">
          <div class="product-label">Batatas pré Pré-frita<br>linha Harbor Fries</div>
          <div class="product-body">
            <div class="product-photo photo-fries" role="img" aria-label="Foto de batatas fritas"></div>
            <p class="product-text">Lorem ipsum dolor sit amet,<br>consectetur adipiscing elit.<br>Phasellus iaculis bibendum auctor.<br>Mauris tempus at nisl vitae lobortis.</p>
          </div>
        </article>
      </div>
    </section>
  </main>
</body>
</html>
```